Organic Herbs & Spices container

Greek startup company, which cultivate and trade spices and herbs (such as oregano, mint, thyme, sage etc.)

At present we are interested in only the type and shape of packaging which should be made by materials such as paper, cardboard, laminated paper and others based on paper or plastic.

Package size vary from 80g (2.82oz) - 300g (10.58oz). We are going to use the same packing for a variety of products with different information

* Please find attached our logo which should be included in the design.
* There is no company name available at the moment, however a name placeholder should be included.
* include a placeholder for the type of product (sage, oregano, mint, tea etc...).
* Each package should have a place in order to include product details and nutrition facts.

e.g.
xxxx (company name placeholder)
Sage (product type)
product details and nutrition facts.
Updates

Dear designers,first of all, thank you for your proposals. Please find bellow some updates for the project.- It is mandatory to include the logo into the design - Each package should be able to stored vertically - We are looking for one specific package design, please do not submit many variations of a certain package neither colour differentiations Thanks and good luck Added Wednesday, September 28, 2016

Please avoid the use of images. The same package will be used for all the kinds of products (only name and maybe colour will be different among different products. A transparent frame that will show the contents could be used too) Added Wednesday, September 28, 2016

Please find attached logo in EPS format

Our logo is the baseline, any concepts should be based on it. Try to avoid just adding the logo as a small sticker somewhere on the design. Please try to create around it at any way toy like. This could be, to visualize it as a 3D shape or object which can be used as the container of the products.

Reason: We would like to extend the time of the project. We believe that most of the submitted designs do not comply with our requirements.

Reason: We would like to see a bigger variety of ideas

Target Market(s)

Pretty much to anyone over 20 years old worldwide.

Industry/Entity Type

Nutrition

Requirements
Must have
• It should be attractive, easily recognized, simple yet innovative, durable, functional (easy to use) and easy to store.
Should not have
• Project must not include complex or obnoxious shapes and colours.

```html
<!DOCTYPE html>
<html lang="en">
<head>
<meta charset="utf-8">
<title>Thyme – Organic Herbs &amp; Spices Pouch</title>
<link href="https://fonts.googleapis.com/css2?family=Playfair+Display:wght@700;900&family=Lato:wght@400;700&display=swap" rel="stylesheet">
<style>
  :root {
    --bg: #ffffff;
    --kraft: #c8a37c;
    --kraft-dark: #b48d64;
    --label-blue: #1ba6dc;
    --ink: #111111;
    --paper: #fbf8f2;
    --herb-green: #5d6b3a;
    --herb-brown: #7a6a45;
    --gold: #c9a227;
  }
  * { box-sizing: border-box; margin: 0; padding: 0; }
  html, body { width: 1200px; height: 816px; overflow: hidden; background: var(--bg); }
  .canvas { position: relative; width: 1200px; height: 816px; }

  .pouch {
    position: absolute;
    background: linear-gradient(180deg, var(--kraft) 0%, var(--kraft-dark) 100%);
    border-radius: 6px;
  }
  .pouch--front { left: 120px; top: 70px; width: 420px; height: 680px; }
  .pouch--back  { left: 660px; top: 70px; width: 420px; height: 680px; }
  .pouch__seal {
    position: absolute; left: 0; right: 0; top: 0; height: 34px;
    border-bottom: 1px solid rgba(0,0,0,0.12);
  }

  /* Front label */
  .front-label {
    position: absolute; left: 40px; top: 70px; width: 340px; height: 258px;
    background: var(--label-blue);
    padding: 10px;
  }
  .front-label__frame {
    position: relative; width: 100%; height: 100%;
    border: 1.5px solid var(--ink);
    text-align: center;
    font-family: "Playfair Display", serif;
    color: var(--ink);
  }
  .front-label__number {
    position: absolute; left: 50%; top: -11px; transform: translateX(-50%);
    width: 40px; height: 36px; background: var(--ink); color: var(--label-blue);
    font-size: 20px; font-weight: 700; line-height: 36px;
  }
  .brand {
    position: absolute; left: 0; right: 0; top: 36px;
    display: flex; align-items: center; justify-content: center; gap: 6px;
    font-family: "Lato", sans-serif; font-weight: 700; font-size: 11px;
    letter-spacing: 1px; color: var(--ink);
  }
  .brand__dot { width: 10px; height: 10px; border-radius: 50%; background: var(--gold); }
  .product-name {
    position: absolute; left: 0; right: 0; top: 78px;
    font-size: 34px; font-weight: 900; letter-spacing: 1px;
  }
  .product-badge {
    position: absolute; left: 50%; top: 130px; transform: translateX(-50%);
    width: 170px; height: 22px; border-radius: 11px; background: var(--ink);
    color: var(--label-blue); font-family: "Lato", sans-serif; font-weight: 700;
    font-size: 12px; letter-spacing: 3px; line-height: 22px;
  }
  .product-category {
    position: absolute; left: 0; right: 0; top: 160px;
    font-family: "Lato", sans-serif; font-weight: 700; font-size: 12px; letter-spacing: 2px;
  }
  .product-weight {
    position: absolute; left: 0; right: 0; bottom: 14px;
    font-family: "Lato", sans-serif; font-weight: 700; font-size: 9px; letter-spacing: 1px;
  }

  .content-window {
    position: absolute; left: 40px; top: 328px; width: 340px; height: 230px;
    background: linear-gradient(160deg, var(--herb-brown) 0%, var(--herb-green) 55%, #4a5630 100%);
  }

  /* Back label */
  .nutrition {
    position: absolute; left: 100px; top: 150px; width: 220px; height: 300px;
    background: var(--paper); padding: 10px 12px;
    font-family: "Lato", sans-serif; color: var(--ink);
  }
  .nutrition__title {
    font-family: "Playfair Display", serif; font-weight: 900; font-size: 20px; line-height: 1;
  }
  .nutrition__basis { font-size: 8px; font-weight: 700; border-bottom: 4px solid var(--ink); padding: 3px 0 2px; }
  .nutrition__table { width: 100%; border-collapse: collapse; font-size: 7.5px; margin-top: 2px; }
  .nutrition__table th { text-align: left; font-weight: 700; padding: 2px 3px; border-bottom: 1px solid var(--ink); }
  .nutrition__table td { padding: 2.5px 3px; border: 1px solid var(--ink); }
</style>
</head>
<body>
<main class="canvas">

  <section class="pouch pouch--front">
    <div class="pouch__seal"></div>
    <div class="front-label">
      <div class="front-label__frame">
        <div class="front-label__number">03</div>
        <div class="brand"><span class="brand__dot"></span><span>HERBARA</span></div>
        <h1 class="product-name">THYME</h1>
        <div class="product-badge">ORGANIC</div>
        <div class="product-category">HERBS &amp; SPICES</div>
        <div class="product-weight">NET WT 85g/3.0oz</div>
      </div>
    </div>
    <div class="content-window" role="img" aria-label="Transparent window showing dried thyme leaves inside the pouch"></div>
  </section>

  <section class="pouch pouch--back">
    <div class="pouch__seal"></div>
    <div class="nutrition">
      <h2 class="nutrition__title">Nutrition Facts</h2>
      <div class="nutrition__basis">per 100g</div>
      <table class="nutrition__table">
        <tr><th>Nutrients</th><th>mg</th><th>Percentage</th></tr>
        <tr><td>Folate</td><td>45 mcg</td><td>11%</td></tr>
        <tr><td>Niacin</td><td>1.8 mg</td><td>12%</td></tr>
        <tr><td>Pantothenic acid</td><td>0.4 mg</td><td>8%</td></tr>
        <tr><td>Pyridoxine</td><td>0.3 mg</td><td>26%</td></tr>
        <tr><td>Riboflavin</td><td>0.5 mg</td><td>36%</td></tr>
        <tr><td>Thiamin</td><td>0.05 mg</td><td>4%</td></tr>
        <tr><td>Vitamin A</td><td>4751 IU</td><td>158%</td></tr>
        <tr><td>Vitamin C</td><td>160 mg</td><td>266%</td></tr>
        <tr><td>Sodium</td><td>9 mg</td><td>1%</td></tr>
        <tr><td>Potassium</td><td>609 mg</td><td>13%</td></tr>
        <tr><td>Calcium</td><td>405 mg</td><td>40%</td></tr>
        <tr><td>Iron</td><td>17 mg</td><td>212%</td></tr>
        <tr><td>Magnesium</td><td>160 mg</td><td>40%</td></tr>
        <tr><td>Zinc</td><td>1.8 mg</td><td>17%</td></tr>
      </table>
    </div>
  </section>

</main>
</body>
</html>
```